Higher co-efficient of performance means more heat for your money

I need a bar graph that will have the following heating systems, 80% efficient gas furnace COP of .8, Electric heat COP of 1, and Our best selling heat pump with a cop of 4 at 47F. I will have a constant bar, 100$ worth of gas for furnace, 100$ of electricity for electric heat, and 100$ worth of electricity for our heat pumps. next to them I will have a bar showing how much heat each heating system will provide for $100 of fuel. For gas furnace I need a bar that says $80 worth of heat and the barograph to match it, for electric heat I need the bar to show 100$ worth of heat, for our best selling heat pump I need the bar graph to show and say $400 dollars worth of heat. Please take a look at my website www.summitbreezecomfort.example for brand color and feel

```html
<!DOCTYPE html>
<html lang="en">
<head>
<meta charset="utf-8">
<title>Higher Coefficient of Performance – Summit Breeze Comfort</title>
<link href="https://fonts.googleapis.com/css2?family=Arimo:wght@400;700&display=swap" rel="stylesheet">
<style>
  :root {
    --brand-blue: #0470bd;
    --brand-red: #c4202e;
    --elec-blue-top: #0e64b8;
    --elec-blue-bottom: #2a4fae;
    --heat-top: #e5502c;
    --heat-mid: #d8352b;
    --heat-bottom: #c92126;
    --track-top: #dcdbdc;
    --track-bottom: #c4c3c5;
    --label-grey: #6d6e71;
    --paper: #ffffff;
  }
  * { margin: 0; padding: 0; box-sizing: border-box; }
  html, body { width: 1200px; height: 1200px; overflow: hidden; background: var(--paper); }
  body { font-family: "Arimo", Arial, sans-serif; }

  .poster {
    position: relative;
    width: 1200px; height: 1200px;
    background: var(--paper);
    border: 12px solid var(--brand-blue);
  }

  .headline {
    position: absolute; left: 56px; top: 56px;
    color: var(--brand-blue);
  }
  .headline__main {
    font-weight: 700; font-size: 57px; line-height: 56px; letter-spacing: -0.5px;
  }
  .headline__sub {
    font-weight: 400; font-size: 37px; line-height: 44px; margin-top: 6px;
  }
  .badge {
    position: absolute; left: 56px; top: 237px;
    width: 385px; height: 48px;
    border-radius: 24px;
    background: linear-gradient(#d22b36, #b81d2a);
    color: #fff; font-size: 26px; line-height: 48px; text-align: center;
    box-shadow: 0 2px 3px rgba(0,0,0,.25);
  }

  .brand {
    position: absolute; left: 786px; top: 130px; width: 334px;
    display: flex; align-items: center; gap: 14px;
    color: var(--brand-blue);
  }
  .brand__dot {
    flex: none; width: 44px; height: 44px; border-radius: 50%;
    background: var(--brand-red);
  }
  .brand__name {
    font-weight: 700; font-size: 34px; line-height: 38px;
  }

  .bar {
    position: absolute; top: 337px; width: 133px; height: 715px;
    background: linear-gradient(90deg, #bdbcbe 0%, var(--track-top) 30%, var(--track-bottom) 100%);
  }
  .bar__fill {
    position: absolute; left: 0; right: 0; bottom: 0;
    color: #fff; text-align: center;
    text-shadow: 0 2px 3px rgba(0,0,0,.45);
  }
  .bar__fill--electric {
    height: 222px;
    background: linear-gradient(var(--elec-blue-top), var(--elec-blue-bottom));
  }
  .bar__fill--heat {
    background: linear-gradient(var(--heat-top), var(--heat-mid) 45%, var(--heat-bottom));
  }
  .amount {
    display: block; font-weight: 700; font-size: 50px; line-height: 50px;
    letter-spacing: -2px; padding-top: 20px;
  }
  .caption {
    display: block; font-weight: 700; font-size: 23px; line-height: 25px; margin-top: 6px;
  }

  .system {
    position: absolute; top: 1075px;
    color: var(--label-grey); font-weight: 700; font-size: 36px; line-height: 41px;
    text-align: center; letter-spacing: -0.5px; transform: translateX(-50%);
    white-space: nowrap;
  }
</style>
</head>
<body>
<main class="poster">
  <header class="headline">
    <h1 class="headline__main">Higher Co-Efficient<br>of Performance</h1>
    <p class="headline__sub">Means More Heat for your Money</p>
  </header>
  <div class="badge">Our Best: COP of 4 at 47°F</div>

  <div class="brand">
    <span class="brand__dot"></span>
    <span class="brand__name">Summit Breeze Comfort</span>
  </div>

  <!-- Gas furnace -->
  <div class="bar" style="left:55px">
    <div class="bar__fill bar__fill--electric">
      <span class="amount">100$</span>
      <span class="caption">worth of<br>Electricity</span>
    </div>
  </div>
  <div class="bar" style="left:203px">
    <div class="bar__fill bar__fill--heat" style="height:173px">
      <span class="amount">80$</span>
      <span class="caption">worth of<br>HEAT</span>
    </div>
  </div>
  <div class="system" style="left:196px">80% GAS<br>FURNACE</div>

  <!-- Electric heat -->
  <div class="bar" style="left:449px">
    <div class="bar__fill bar__fill--electric">
      <span class="amount">100$</span>
      <span class="caption">worth of<br>Electricity</span>
    </div>
  </div>
  <div class="bar" style="left:597px">
    <div class="bar__fill bar__fill--heat" style="height:222px">
      <span class="amount">100$</span>
      <span class="caption">worth of<br>HEAT</span>
    </div>
  </div>
  <div class="system" style="left:588px">ELECTRIC<br>HEAT</div>

  <!-- Heat pump -->
  <div class="bar" style="left:839px">
    <div class="bar__fill bar__fill--electric">
      <span class="amount">100$</span>
      <span class="caption">worth of<br>Electricity</span>
    </div>
  </div>
  <div class="bar" style="left:987px">
    <div class="bar__fill bar__fill--heat" style="height:713px">
      <span class="amount" style="padding-top:22px">400$</span>
      <span class="caption">worth of<br>HEAT</span>
    </div>
  </div>
  <div class="system" style="left:981px">OUR BEST SELLING<br>HEAT PUMP</div>
</main>
</body>
</html>
```